Fresh Start Bold Body Challenge 2017 Poster

We are having a Fresh Start, Bold Body Challenge for 2017 at our fitness studio. We need a poster design using the template attached as a reference (Only reference). I have also included our Vorbelix logo to put on the poster. Please DO NOT use the graphics in the flyer as we are expecting something much much better :-)
MUST HAVES:
- Size needed 11x17 with bleeding for printing
- .PSD File Format WITH LAYERS (CS3 Compatible)*** A MUST
- Use Vorbelix Bootcamps Logo
- Use Information in the attached word doc

```html
<!DOCTYPE html>
<html lang="en">
<head>
<meta charset="utf-8">
<title>Fresh Start, Bold Body Challenge 2017 – Vorbelix Bootcamps</title>
<link rel="stylesheet" href="https://fonts.googleapis.com/css2?family=Alfa+Slab+One&family=Arimo:wght@700&family=Aladin&family=Creepster&display=swap">
<style>
  :root {
    --orange: #ff6a13;
    --blue: #2f74bf;
    --footer: #22251d;
    --white: #ffffff;
    --gold: #f5c400;
    --gold-edge: #6b5200;
    --value-grey: #e6e2dc;
    --ink: #111111;
    --finale-red: #7a0f0f;
    --price-red: #e8170c;
    --prize-orange: #ff6a13;
    --veil: rgba(215, 215, 215, 0.7);
  }
  * { margin: 0; padding: 0; box-sizing: border-box; }
  html, body { width: 776px; height: 1200px; overflow: hidden; background: var(--white); }
  .poster { position: relative; width: 776px; height: 1200px; overflow: hidden; font-family: "Arimo", Arial, sans-serif; }

  .title-band {
    position: absolute; left: 0; top: 0; width: 776px; height: 152px;
    background: var(--orange);
    display: flex; align-items: center; justify-content: center;
  }
  .title {
    font-family: "Alfa Slab One", serif; color: var(--white); font-weight: 400;
    font-size: 44px; line-height: 56px; text-align: center; letter-spacing: 0.5px;
  }

  .hero {
    position: absolute; left: 0; top: 152px; width: 776px; height: 500px;
    background:
      radial-gradient(ellipse 260px 300px at 600px 210px, #b98f73 0%, rgba(185,143,115,0) 70%),
      linear-gradient(170deg, #7d7b78 0%, #9a918a 30%, #8a7468 55%, #4a423d 80%, #2e2a27 100%);
  }
  .tagline-veil {
    position: absolute; left: 0; top: 152px; width: 776px; height: 90px;
    background: var(--veil);
    display: flex; align-items: center; justify-content: center;
  }
  .tagline {
    font-weight: 700; color: var(--gold);
    font-size: 31px; line-height: 40px; text-align: center;
    text-shadow: 1px 1px 0 var(--gold-edge), -1px -1px 0 var(--gold-edge), 1px -1px 0 var(--gold-edge), -1px 1px 0 var(--gold-edge);
  }

  .brand-card {
    position: absolute; z-index: 2; left: 36px; top: 440px; width: 494px; height: 232px;
    background: var(--white); border: 10px solid var(--ink); border-radius: 14px;
    display: flex; align-items: center; justify-content: center; gap: 16px;
  }
  .brand-mark { width: 32px; height: 32px; background: var(--blue); }
  .brand-name { font-weight: 700; color: var(--ink); font-size: 42px; line-height: 1; }

  .schedule-band {
    position: absolute; left: 0; top: 652px; width: 776px; height: 227px;
    background: var(--orange);
    display: flex; flex-direction: column; align-items: center; padding-top: 44px;
  }
  .schedule-line { font-size: 29px; line-height: 40px; font-weight: 700; text-align: center; }
  .schedule-label { color: var(--ink); }
  .schedule-value { color: var(--value-grey); }
  .finale {
    font-family: "Alfa Slab One", serif; font-weight: 400; color: var(--finale-red);
    font-size: 35px; line-height: 50px;
  }

  .offer-band {
    position: absolute; left: 0; top: 879px; width: 776px; height: 268px;
    background: var(--blue);
    display: flex; flex-direction: column; align-items: center; padding-top: 22px;
  }
  .offer {
    font-family: "Aladin", cursive; color: var(--white);
    font-size: 42px; line-height: 58px; text-align: center; letter-spacing: 1px;
  }
  .offer-price { font-family: "Arimo", Arial, sans-serif; font-weight: 700; color: var(--price-red); font-size: 46px; }
  .prize { margin-top: 20px; display: flex; align-items: baseline; gap: 14px; }
  .prize-amount { font-weight: 700; color: var(--prize-orange); font-size: 72px; line-height: 1; }
  .prize-text { font-family: "Creepster", cursive; color: var(--white); font-size: 50px; line-height: 1; }

  .footer-band {
    position: absolute; left: 0; top: 1147px; width: 776px; height: 53px;
    background: var(--footer);
    display: flex; align-items: center; justify-content: center;
  }
  .footer-text { color: var(--gold); font-weight: 700; font-size: 22px; }
</style>
</head>
<body>
<main class="poster">
  <header class="title-band">
    <h1 class="title">FRESH START, BOLD BODY<br>CHALLENGE</h1>
  </header>

  <div class="hero" role="img" aria-label="Photo of a determined athlete in a push-up position"></div>

  <div class="tagline-veil">
    <p class="tagline">In Just 6 Weeks, Transform Your Body<br>And Get In The Best Shape Of Your Life!</p>
  </div>

  <section class="schedule-band">
    <p class="schedule-line"><span class="schedule-label">Kick Off Meeting:</span> <span class="schedule-value">Thursday, Jan 12th at 7:30 pm</span></p>
    <p class="schedule-line"><span class="schedule-label">Start Date:</span> <span class="schedule-value">Tuesday, January 17th</span></p>
    <p class="schedule-line"><span class="schedule-label">End Date:</span> <span class="schedule-value">Saturday, February 25th</span></p>
    <p class="finale">Finale Party March 2nd</p>
  </section>

  <div class="brand-card">
    <span class="brand-mark"></span>
    <span class="brand-name">Vorbelix Bootcamps</span>
  </div>

  <section class="offer-band">
    <p class="offer">6 Weeks of Training, Nutrition, and<br>Coaching Starting at just <span class="offer-price">$99!</span></p>
    <p class="prize"><span class="prize-amount">$500</span><span class="prize-text">CASH Prize for Winner!</span></p>
  </section>

  <footer class="footer-band">
    <p class="footer-text">Visit www.vorbelixbootcamps.com FOR MORE INFO</p>
  </footer>
</main>
</body>
</html>
```